Pop punk gig poster design!

In need of an amazing poster design for a gig We are organising, the genre is pop punk, and will be an all ages gig. I need to it bold, random and capture the eye of any bypasses, and make people want to go to the gig just because the poster is awesome! The event will be called "A night of comets" and will consist of three bands and an acoustic set to open. All the bands are full of energy and create an unreal ambiance during there shows, I would like to capture that in the poster. Open to anything spectacular, the sky is the limit.

Requirements
Must have
• I need to have the name of the event "A Night Of Comets"
Band names(in this order):
-Turn the Dial
-Frozen Fenwick
-Wilma's Lantern
-Loralie Pettigrew

Date: Saturday 10th November 2012
Time: 5:15pm
Venue: The Kiln, 47 Tamsin street, West End, QLD 4101
Ticket price: $10+bf online
$15 at the door.
Free BBQ

```html
<!DOCTYPE html>
<html lang="en">
<head>
<meta charset="utf-8">
<title>A Night Of Comets – Gig Poster</title>
<link rel="stylesheet" href="https://fonts.googleapis.com/css2?family=Fredoka:wght@400;500;600;700&family=Rubik+Dirt&display=swap">
<style>
  :root {
    --night: #221e1b;
    --glow-core: #f8ef3e;
    --glow-mid: #f4b82b;
    --glow-edge: #e48a1d;
    --glow-dusk: #6b4a22;
    --flare: #e2481d;
    --tag: #e0501f;
    --ink: #111111;
    --skyline: #0c0a09;
    --paper: #ffffff;
  }
  html, body {
    margin: 0;
    padding: 0;
    width: 849px;
    height: 1200px;
    overflow: hidden;
    background: var(--night);
  }
  .poster {
    position: relative;
    width: 849px;
    height: 1200px;
    overflow: hidden;
    background:
      radial-gradient(ellipse 600px 880px at 50% 82%,
        var(--glow-core) 0%,
        var(--glow-mid) 40%,
        var(--glow-edge) 64%,
        var(--glow-dusk) 84%,
        var(--night) 100%);
  }
  .stage-art {
    position: absolute;
    left: 90px;
    top: 380px;
    width: 640px;
    height: 790px;
    background: radial-gradient(ellipse 55% 60% at 50% 55%,
      rgba(226, 72, 29, 0.32) 0%,
      rgba(226, 72, 29, 0.14) 55%,
      rgba(226, 72, 29, 0) 100%);
  }
  .skyline-art {
    position: absolute;
    left: 0;
    top: 1128px;
    width: 849px;
    height: 72px;
    background: var(--skyline);
  }
  .title-bar {
    position: absolute;
    left: 81px;
    top: 162px;
    width: 647px;
    height: 112px;
    background: var(--ink);
    transform: rotate(-5deg);
    display: flex;
    align-items: center;
    justify-content: center;
  }
  .title-main {
    margin: 0;
    font-family: "Rubik Dirt", sans-serif;
    font-weight: 400;
    font-size: 104px;
    line-height: 1;
    color: var(--paper);
    white-space: nowrap;
  }
  .title-sub {
    position: absolute;
    left: 255px;
    top: 288px;
    width: 360px;
    text-align: center;
    font-family: "Rubik Dirt", sans-serif;
    font-size: 74px;
    line-height: 1;
    color: var(--ink);
    transform: rotate(-6deg);
  }
  .band {
    position: absolute;
    height: 62px;
    background: var(--tag);
    box-shadow: 3px 4px 6px rgba(0,0,0,0.55);
    display: flex;
    align-items: center;
    justify-content: center;
    font-family: "Fredoka", sans-serif;
    font-weight: 500;
    font-size: 42px;
    color: var(--ink);
    white-space: nowrap;
  }
  .band--opener   { left: 103px; top: 466px; width: 400px; transform: rotate(-5deg); }
  .band--second   { left: 400px; top: 582px; width: 350px; transform: rotate(5deg); font-size: 38px; }
  .band--third    { left: 148px; top: 680px; width: 342px; transform: rotate(-4deg); font-size: 38px; }
  .band--headline { left: 262px; top: 820px; width: 420px; transform: rotate(4deg); font-size: 38px; }
  .free-bbq {
    position: absolute;
    left: 548px;
    top: 450px;
    width: 210px;
    text-align: center;
    white-space: nowrap;
    font-family: "Fredoka", sans-serif;
    font-weight: 700;
    font-size: 40px;
    line-height: 1.2;
    color: var(--paper);
    transform: rotate(5deg);
    -webkit-text-stroke: 1.5px var(--ink);
    text-shadow: 3px 3px 0 var(--ink);
  }
  .details {
    position: absolute;
    left: 0;
    width: 849px;
    margin: 0;
    text-align: center;
    white-space: nowrap;
    font-family: "Fredoka", sans-serif;
    line-height: 1.2;
    color: var(--paper);
    text-shadow: 2px 3px 0 var(--ink), 0 0 4px var(--ink);
  }
  .details--date  { top: 958px;  font-size: 37px; font-weight: 600; }
  .details--time  { top: 1026px; font-size: 42px; font-weight: 600; }
  .details--venue { top: 1092px; font-size: 27px; font-weight: 600; }
  .details--price { top: 1140px; font-size: 21px; font-weight: 500; }
</style>
</head>
<body>
<main class="poster">
  <div class="stage-art" role="img" aria-label="Large orange A emblem with spotlight beams behind the line-up"></div>
  <div class="skyline-art" role="img" aria-label="Dark city skyline silhouette along the bottom edge"></div>

  <div class="title-bar"><h1 class="title-main">A NIGHT OF</h1></div>
  <div class="title-sub">COMETS</div>

  <div class="band band--opener">Turn the Dial</div>
  <div class="free-bbq">Free BBQ</div>
  <div class="band band--second">Frozen Fenwick</div>
  <div class="band band--third">Wilma's Lantern</div>
  <div class="band band--headline">Loralie Pettigrew</div>

  <p class="details details--date">Saturday 10th November 2012</p>
  <p class="details details--time">at 5:15pm</p>
  <p class="details details--venue">The Kiln, 47 Tamsin street, West End, QLD 4101</p>
  <p class="details details--price">Ticket price: $10+bf online, $15 at the door</p>
</main>
</body>
</html>
```